stonewick For High end Builder/developer construction

We will be a residential building company focused on a meticulous approach to high end quality builds with a design collaborative approach with all our clients to push the boundaries on new forms, products and bespoke architectural designs.

We want to be known to thrives upon collaboration with architects, designers and our clients to help them transform big ideas into inspiring spaces. We run every part of the building process, from planning through to construction and completion, is detail-focused and seamlessly managed.

Target Market(s)

High end

Font styles to use
Other font styles liked:
• Gotham Light

Colors

Designer to choose only greyscale colors for use in the design.

Requirements
Must have
• Bold headed incorporating sharp features for the logo to standout in mostly black to ensure the logo pops

```html
<!DOCTYPE html>
<html lang="en">
<head>
<meta charset="utf-8">
<title>Stonewick Letterhead</title>
<link rel="stylesheet" href="https://fonts.googleapis.com/css2?family=Lato:wght@400&family=Montserrat:wght@400;500&display=swap">
<style>
  :root {
    --backdrop: #d6d6d6;
    --paper: #ffffff;
    --ink: #111111;
    --text: #555555;
    --accent: #8e8e8e;
    --watermark: #eeeeee;
  }
  * { margin: 0; padding: 0; box-sizing: border-box; }
  html, body {
    width: 1056px;
    height: 1200px;
    overflow: hidden;
    background: var(--backdrop);
  }
  .letterhead {
    position: absolute;
    left: 125px;
    top: 30px;
    width: 806px;
    height: 1140px;
    background: var(--paper);
    overflow: hidden;
  }
  .brand {
    position: absolute;
    left: 74px;
    top: 64px;
    width: 170px;
    display: flex;
    flex-direction: column;
    align-items: center;
  }
  .brand-square {
    width: 62px;
    height: 62px;
    background: var(--ink);
  }
  .brand-name {
    margin-top: 22px;
    font-family: "Montserrat", sans-serif;
    font-weight: 400;
    font-size: 15px;
    letter-spacing: 3.4px;
    color: var(--ink);
    white-space: nowrap;
  }
  .contact {
    position: absolute;
    left: 556px;
    top: 68px;
    font-family: "Lato", sans-serif;
    font-style: normal;
    font-weight: 400;
    font-size: 15px;
    line-height: 18px;
    color: var(--text);
    white-space: nowrap;
  }
  .contact-address { margin-bottom: 9px; }
  .contact-row {
    display: flex;
    align-items: center;
    height: 21px;
  }
  .contact-icon {
    width: 14px;
    height: 14px;
    margin-right: 14px;
    flex: none;
  }
  .watermark {
    position: absolute;
    left: 0;
    width: 100%;
    top: 630px;
    text-align: center;
    font-family: "Montserrat", sans-serif;
    font-weight: 500;
    font-size: 92px;
    letter-spacing: 6px;
    color: var(--watermark);
    white-space: nowrap;
  }
  .footer-band {
    position: absolute;
    left: 0;
    bottom: 0;
    width: 806px;
    height: 17px;
  }
</style>
</head>
<body>
  <main class="letterhead">
    <header>
      <div class="brand">
        <div class="brand-square" aria-hidden="true"></div>
        <div class="brand-name">STONEWICK</div>
      </div>

      <address class="contact">
        <div class="contact-address">
          1234 First Line Address<br>
          5678 Second Line Address
        </div>
        <div class="contact-row">
          <svg class="contact-icon" viewBox="0 0 16 16" aria-hidden="true">
            <path d="M3.5 1.5 L6 4.5 L4.6 6.2 C5.4 8 7.2 9.9 9.5 11.2 L11.2 9.8 L14.3 12.3 L12.7 14.5 C7 13.8 2.2 9 1.5 3.2 Z" fill="none" stroke="var(--accent)" stroke-width="1.6" stroke-linejoin="round"/>
            <path d="M9.5 2.5 A4 4 0 0 1 13.5 6.5 M9.5 0.5 A6 6 0 0 1 15.5 6.5" fill="none" stroke="var(--accent)" stroke-width="1.2"/>
          </svg>
          <span>(777) 888-7777</span>
        </div>
        <div class="contact-row">
          <svg class="contact-icon" viewBox="0 0 16 16" aria-hidden="true">
            <rect x="0.5" y="3" width="15" height="10" fill="var(--accent)"/>
            <path d="M0.5 3 L8 9 L15.5 3 M0.5 13 L6 8 M15.5 13 L10 8" fill="none" stroke="#ffffff" stroke-width="1.1"/>
          </svg>
          <span>info@yourmail.com</span>
        </div>
        <div class="contact-row">
          <svg class="contact-icon" viewBox="0 0 16 16" aria-hidden="true">
            <circle cx="8" cy="8" r="6.8" fill="none" stroke="var(--accent)" stroke-width="1.2"/>
            <ellipse cx="8" cy="8" rx="3" ry="6.8" fill="none" stroke="var(--accent)" stroke-width="0.9"/>
            <path d="M1.2 8 H14.8 M2.3 4.5 H13.7 M2.3 11.5 H13.7" stroke="var(--accent)" stroke-width="0.9"/>
          </svg>
          <span>www.yourwebsite.com</span>
        </div>
      </address>
    </header>

    <div class="watermark" aria-hidden="true">STONEWICK</div>

    <svg class="footer-band" viewBox="0 0 806 17" preserveAspectRatio="none" aria-hidden="true">
      <polygon points="0,0 408,0 399,17 0,17" fill="var(--ink)"/>
      <polygon points="417,0 806,0 806,17 408,17" fill="var(--accent)"/>
    </svg>
  </main>
</body>
</html>
```